Brand new leaflet design creative ideas.

I need a flyer designed for my business

I run a pay weekly carpet business and need designs for a flyer this design i will also want to enable it on letterheads business cards and a logo from it when created.

my domain name is www.pallowmere.co.uk / www.pallowmere.com

Our main competitor i have attached his design to this brief to give you a bit of an idea on how we work, however i do not want a copycat design i want a brand new design something not like theres but eye catching direct to the point.

We are open to colour suggestions as long as the colours work.
Thank you.

Target Market(s)

This print material will be delivered to customers houses.

Industry/Entity Type

Flooring

Font styles to use
Serif
Sans Serif

Requirements
Must have
• Website domain name,
• Various print options CMYK, PDF
Nice to have
• Creativity eye catching
Should not have
• SHOULD NOT BE A COPYCAT DESIGN SOMETHING NEW & CREATIVE

```html
<!DOCTYPE html>
<html lang="en">
<head>
<meta charset="utf-8">
<title>Pallowmere Pay Weekly Flyer</title>
<link rel="stylesheet" href="https://fonts.googleapis.com/css2?family=Lato:wght@400;700;900&family=Open+Sans:wght@400;600;700&family=Roboto:wght@900&display=swap">
<style>
  :root {
    --red: #e3202a;
    --ink: #1d1d1d;
    --charcoal: #333335;
    --paper: #f4f4f4;
    --stage: #e9e9e7;
    --white: #ffffff;
  }
  * { box-sizing: border-box; margin: 0; padding: 0; }
  html, body { width: 1200px; height: 1200px; overflow: hidden; background: var(--stage); }
  .flyer {
    position: absolute; left: 180px; top: 6px;
    width: 806px; height: 1140px;
    transform: scale(1.042); transform-origin: 0 0;
    background: linear-gradient(180deg, #ffffff 0%, var(--paper) 60%, #ececec 100%);
    box-shadow: 0 6px 18px rgba(0,0,0,.18);
    overflow: hidden;
    font-family: 'Lato', sans-serif; color: var(--ink);
  }
  .shapes { position: absolute; inset: 0; }
  .pay-badge {
    position: absolute; left: 485px; top: 190px; width: 280px; height: 280px;
    text-align: center;
  }
  .pay-badge .pay { position: absolute; left: 0; right: 0; top: 78px; font-family: 'Roboto', sans-serif; font-weight: 900; font-size: 98px; line-height: 1; letter-spacing: 2px; color: #000; }
  .pay-badge .weekly { position: absolute; left: 0; right: 0; top: 168px; font-family: 'Lato', sans-serif; font-weight: 900; font-size: 46px; line-height: 1; color: var(--red); }
  .brand { position: absolute; left: 68px; top: 508px; display: flex; align-items: center; gap: 10px; }
  .brand-dot { width: 40px; height: 40px; border-radius: 50%; background: var(--red); }
  .brand-name { font-family: 'Lato', sans-serif; font-weight: 900; font-size: 50px; color: var(--red); line-height: 1; }
  .intro { position: absolute; left: 66px; top: 610px; width: 314px; font-family: 'Open Sans', sans-serif; font-size: 13.5px; line-height: 18px; text-align: justify; color: #222; }
  .benefits { position: absolute; left: 446px; top: 512px; list-style: none; }
  .benefits li { display: flex; align-items: center; height: 44.5px; font-size: 28px; color: #222; }
  .benefits .icon { width: 26px; height: 26px; border-radius: 50%; background: var(--red); color: var(--white); font-size: 14px; font-weight: 900; display: flex; align-items: center; justify-content: center; margin-right: 11px; }
  .selected { position: absolute; left: 189px; top: 701px; width: 164px; height: 164px; border-radius: 50%; background: var(--white); border: 3px solid var(--red); text-align: center; }
  .selected .congrats { margin-top: 42px; font-size: 14px; font-weight: 900; color: var(--red); letter-spacing: .5px; }
  .selected .you { font-size: 32px; line-height: 32px; margin-top: 2px; }
  .selected .been { font-size: 21px; line-height: 22px; }
  .contact { position: absolute; left: 460px; top: 893px; width: 336px; text-align: center; color: var(--white); }
  .contact .call { font-size: 31px; font-weight: 700; line-height: 1; }
  .credit-box { margin: 16px 0 0 5px; width: 318px; height: 82px; background: var(--red); border: 2px dashed var(--white); outline: 3px solid var(--red); display: flex; align-items: center; justify-content: center; gap: 10px; }
  .credit-box .label { font-size: 25px; }
  .credit-box .amount { font-size: 52px; line-height: 1; }
  .contact .apply { margin-top: 18px; font-size: 19.5px; }
  .contact .follow { margin-top: 14px; font-size: 19px; font-weight: 700; }
  .contact .follow .network { color: #3b5fb0; font-weight: 900; font-size: 26px; margin-left: 8px; }
</style>
</head>
<body>
<main class="flyer">
  <svg class="shapes" viewBox="0 0 806 1140" width="806" height="1140">
    <!-- hero photo area -->
    <polygon points="0,0 806,0 806,345 262,455 0,248" fill="#cdbfb0"/>
    <rect role="img" aria-label="Photo: a woman lying on a cream shaggy rug in a living room, browsing a tablet beside a beige sofa" x="0" y="0" width="0" height="0"/>
    <polygon points="0,0 806,0 806,345 262,455 0,248" fill="url(#heroGrad)" role="img" aria-label="Photo: a woman lying on a cream shaggy rug in a living room, browsing a tablet beside a beige sofa"/>
    <polyline points="0,250 262,455 806,345" fill="none" stroke="#111" stroke-width="6"/>
    <polygon points="0,272 0,298 235,448 246,440" fill="var(--red)"/>
    <polygon points="700,385 806,362 806,392 720,405" fill="var(--red)"/>
    <!-- lower photo area -->
    <polygon points="0,786 185,728 470,1140 0,1140" fill="url(#lowerGrad)" role="img" aria-label="Photo: a smiling blonde woman resting her chin on her hands on a soft carpet"/>
    <polygon points="0,760 0,776 150,726 145,718" fill="var(--red)"/>
    <polyline points="0,790 185,728 455,1140" fill="none" stroke="#111" stroke-width="5"/>
    <polygon points="285,872 296,866 478,1140 462,1140" fill="var(--red)"/>
    <!-- contact panel -->
    <polygon points="483,875 806,875 806,1128 470,1128 326,922 453,922" fill="var(--charcoal)"/>
    <!-- pay badge rings -->
    <circle cx="625" cy="330" r="140" fill="var(--red)"/>
    <circle cx="625" cy="330" r="134" fill="var(--white)"/>
    <circle cx="625" cy="330" r="128" fill="#000"/>
    <circle cx="625" cy="330" r="119" fill="var(--white)"/>
    <defs>
      <linearGradient id="heroGrad" x1="0" y1="0" x2="0" y2="1">
        <stop offset="0" stop-color="#d9cfc4"/>
        <stop offset=".5" stop-color="#c9b6a6"/>
        <stop offset="1" stop-color="#efebe6"/>
      </linearGradient>
      <linearGradient id="lowerGrad" x1="0" y1="0" x2="1" y2="1">
        <stop offset="0" stop-color="#f3ede6"/>
        <stop offset=".5" stop-color="#e6d6c4"/>
        <stop offset="1" stop-color="#d8d2cc"/>
      </linearGradient>
    </defs>
  </svg>

  <div class="pay-badge">
    <div class="pay">PAY</div>
    <div class="weekly">WEEKLY</div>
  </div>

  <div class="brand">
    <span class="brand-dot"></span>
    <span class="brand-name">pallowmere</span>
  </div>

  <p class="intro">We are a small family owned and run a pay weekly carpet business that pride ourselves on offering our customers a genuine high quality product and service.</p>

  <ul class="benefits">
    <li><span class="icon">%</span>Interest Free Credit</li>
    <li><span class="icon">£</span>Pay only £10 per week</li>
    <li><span class="icon">✕</span>No Credit Check</li>
    <li><span class="icon">⌂</span>Free Home Measuring</li>
    <li><span class="icon">≡</span>Free Underlay</li>
    <li><span class="icon">✓</span>Free Grippers</li>
    <li><span class="icon">▯</span>Free Door Trims</li>
  </ul>

  <div class="selected">
    <div class="congrats">Congratulations</div>
    <div class="you">You Have</div>
    <div class="been">Been Selected</div>
  </div>

  <div class="contact">
    <div class="call">CALL:000-000-0000</div>
    <div class="credit-box"><span class="label">Credit Limit Is</span><span class="amount">£500</span></div>
    <div class="apply">Apply Online: www.pallowmere.com</div>
    <div class="follow">Follow Us:<span class="network">Friendwall</span></div>
  </div>
</main>
</body>
</html>
```